Real estate sales brochure-Quorlanta

It need to be a real estate sales brochure. A template how I can always adapt the object. In the appendix a sample, please different structure and different design.

Target Market(s)

beautiful presentation of the properties for sale, a Word template

Industry/Entity Type

Real estate

Font styles to use
Serif
Sans Serif

Colors

Designer to choose colors to be used in the design.

Requirements
Must have
• DIN A4 format, Picture not all but some https://files.brevonsa.net/shared/folders/482kQpL2xWmT4vNz7RbY3-cHd9sJf6gA1eUo?mode=viewing
Nice to have
• Color: R187, G214, B: 49 or R119, G187, B66, space for picutre and text

```html
<!DOCTYPE html>
<html lang="de">
<head>
<meta charset="utf-8">
<title>Quorlanta – Verkaufsbroschüre</title>
<link href="https://fonts.googleapis.com/css2?family=Raleway:ital,wght@0,300;0,400;0,500;0,700;0,800;1,800&family=Montserrat:wght@600&display=swap" rel="stylesheet">
<style>
:root{
  --lime:#bbd631;
  --green:#77bb42;
  --deep:#4fa83a;
  --ink:#555;
  --soft:#8a8a8a;
  --faint:#ececec;
  --stage:#2e2e2e;
  --paper:#fff;
}
*{margin:0;padding:0;box-sizing:border-box}
html,body{width:1200px;height:856px;overflow:hidden;background:var(--stage)}
body{position:relative;font-family:"Raleway",sans-serif;color:var(--ink)}
.page{position:absolute;width:222px;height:311px;background:var(--paper);overflow:hidden}
.p1{left:84px;top:84px}.p2{left:353px;top:84px}.p3{left:619px;top:84px}.p4{left:886px;top:84px}
.p5{left:84px;top:457px}.p6{left:353px;top:457px}.p7{left:619px;top:457px}.p8{left:886px;top:457px}
.abs{position:absolute}
.shapes{position:absolute;left:0;top:0}
.photo{position:absolute}
.framed{position:absolute;border:1px solid #cfcfcf;padding:3px;background:#fff}
.framed .photo{position:static;width:100%;height:100%}
.circle{position:absolute;border-radius:50%;border:3px solid #fff}
.brand{font-family:"Raleway",sans-serif;font-weight:700;color:var(--green);white-space:nowrap;line-height:1}
.brand-faint{font-family:"Raleway",sans-serif;font-weight:700;color:var(--faint);white-space:nowrap;line-height:1}
.footer-url{position:absolute;left:22px;top:297px;font-size:3.6px;letter-spacing:2.2px;color:var(--green)}
.footer-brand{position:absolute;right:9px;top:291px;font-size:9px}
.footer-rule{position:absolute;left:15px;right:0;top:306px;height:1px;background:var(--green)}
.footer-rule::before,.rule::before{content:"";position:absolute;left:-2px;top:-1.5px;width:4px;height:4px;border-radius:50%;background:var(--green)}
.rule{position:absolute;height:1px;background:var(--green)}
.rule.center::before{left:50%;margin-left:-2px}
.head{position:absolute;font-weight:700;color:var(--green);text-transform:uppercase;letter-spacing:-.1px;white-space:nowrap}
.body{position:absolute;font-size:3.3px;line-height:5.4px;color:var(--soft);text-align:justify}
.body p{margin-bottom:5px}
.label{position:absolute;font-size:4.2px;font-weight:500;color:var(--green)}
/* cover */
.cover-title{position:absolute;right:20px;font-weight:300;color:#6b6b6b;font-size:15.5px;white-space:nowrap;letter-spacing:-.2px}
.cover-sale{position:absolute;right:20px;top:240px;font-weight:800;font-style:italic;color:var(--lime);font-size:24px;letter-spacing:2px}
/* bullets */
.facts{position:absolute;left:17px;top:178px;list-style:none}
.facts li{font-family:"Montserrat",sans-serif;font-weight:600;font-size:5.6px;letter-spacing:.5px;color:#555;height:24.5px}
.facts li::before{content:"•";margin-right:6px;color:#777}
.facts li span{font-family:"Raleway",sans-serif;font-weight:400;letter-spacing:0;color:#777}
/* contact */
.contact-name{position:absolute;left:112px;top:241px;font-size:10.5px;font-weight:300;color:var(--green)}
.contact-role{position:absolute;left:112px;top:253px;font-size:5.5px;color:#777}
.contact-list{position:absolute;left:112px;top:266px;list-style:none}
.contact-list li{display:flex;align-items:center;font-size:5.5px;color:#666;height:8.5px}
.contact-list svg{margin-right:3px}
</style>
</head>
<body>

<!-- Cover -->
<section class="page p1">
  <svg class="shapes" width="222" height="311" viewBox="0 0 222 311">
    <defs><linearGradient id="coverPhoto" x1="0" y1="0" x2="1" y2="1"><stop offset="0" stop-color="#5fb646"/><stop offset="1" stop-color="#3d9a36"/></linearGradient></defs>
    <polygon points="0,0 205,0 84,170 0,92" fill="url(#coverPhoto)" role="img" aria-label="Foto der Hausfassade mit Garten, grün getönt"/>
    <polygon points="0,88 84,172 205,0 222,0 222,6 78,177 0,108" fill="var(--lime)"/>
    <polygon points="0,108 78,177 74,185 0,125" fill="var(--green)"/>
  </svg>
  <div class="brand abs" style="left:11px;top:14px;font-size:23px;color:#fff">Quorlanta</div>
  <div class="circle" role="img" aria-label="Foto eines modernen weissen Einfamilienhauses am Hang" style="left:117px;top:98px;width:78px;height:78px;background:radial-gradient(circle at 50% 40%,#e9ecef,#8fb27a 70%,#5c8a45)"></div>
  <div class="cover-title" style="top:182px">BEAUTIFUL PRESENTATION</div>
  <div class="rule" style="left:16px;right:0;top:207px"></div>
  <div class="cover-title" style="top:214px">OF THE PROPERTIES</div>
  <div class="rule" style="left:62px;right:0;top:237px"></div>
  <div class="cover-sale">FOR SALE</div>
  <div class="brand-faint abs" style="left:6px;top:276px;font-size:34px;color:#f3f3f3">Quorlanta</div>
</section>

<!-- Location -->
<section class="page p2">
  <div class="brand-faint abs" style="left:45px;top:18px;font-size:23px">Quorlanta</div>
  <div class="framed" style="left:33px;top:51px;width:160px;height:112px">
    <div class="photo" role="img" aria-label="Luftbildkarte des Quartiers am Seeufer" style="background:linear-gradient(160deg,#7b8f5c 0%,#9a9a8a 45%,#6d7c6a 65%,#2f6f78 100%)"></div>
  </div>
  <ul class="facts">
    <li>Ihr neues Zuhause, <span>Rebhaldenweg 4, 8790 Lindenau</span></li>
    <li>Bushaltestelle / S-Bahnhof</li>
    <li>Einkaufsmöglichkeiten</li>
    <li>Schule &amp; Kindergarten</li>
    <li>Strandbadipsum</li>
  </ul>
  <div class="footer-url">www.quorlanta.com</div>
  <div class="brand footer-brand">Quorlanta</div>
  <div class="footer-rule"></div>
</section>

<!-- Community facts -->
<section class="page p3">
  <svg class="shapes" width="222" height="311" viewBox="0 0 222 311">
    <polygon points="0,0 60,0 18,128 0,96" fill="var(--lime)"/>
    <polygon points="60,0 90,0 22,126 18,128" fill="var(--green)"/>
  </svg>
  <div class="circle" role="img" aria-label="Foto der Dorfkirche" style="left:54px;top:20px;width:56px;height:56px;background:linear-gradient(#a9c7e6,#e8edf0 55%,#6d9c4a)"></div>
  <div class="circle" role="img" aria-label="Foto des Seeufers" style="left:30px;top:78px;width:46px;height:46px;background:linear-gradient(#c8d6e2,#d9d6cc 55%,#4d6f7e)"></div>
  <div class="brand-faint abs" style="left:121px;top:40px;font-size:15px">Quorlanta</div>
  <div class="framed" style="left:119px;top:60px;width:89px;height:59px;border-color:var(--lime)">
    <div class="photo" role="img" aria-label="Foto der Häuserzeile am Hafen" style="background:linear-gradient(#6fa0d6,#e6e4dc 55%,#3f6a88)"></div>
  </div>
  <div class="head" style="left:21px;top:133px;font-size:7px">Daten und Fakten zur Gemeinde</div>
  <div class="body" style="left:21px;top:146px;width:184px;line-height:8.7px">
    <p>Lindenau – unverwechselbar, sympathisch, echt – mit diesen Worten wirbt die Seegemeinde für ihre Qualitäten. Trotz der Nähe zur Stadt hat sich der Ort seine Eigenständigkeit bewahrt und gilt als eine der beliebtesten Wohngemeinden am See.</p>
    <p>Die sonnenverwöhnte Lage, gute Verkehrsanbindungen sowie die kulturelle Vielfalt sprechen für sich. Geniessen Sie die Sommermonate im Strandbad, stöbern Sie in den Läden und speisen Sie in einem der vielen Restaurants.</p>
    <p>Lindenau bietet viele attraktive Wander- und Walkingrouten, diverse Reitställe, einen Fussballverein, einen Tennisclub, einen Segelclub und vieles mehr.</p>
    <p>Die Hänge werden seit Generationen für Weinsorten genutzt. Der See als Wärmespeicher und die milden Winde schaffen ideale Bedingungen für den Rebbau. Die Rebberge der Gemeinde wurden vor Jahren durch die Gemeindeversammlung unter Schutz gestellt.</p>
  </div>
  <div class="footer-url">www.quorlanta.com</div>
  <div class="brand footer-brand">Quorlanta</div>
  <div class="footer-rule"></div>
</section>

<!-- Short description -->
<section class="page p4">
  <div class="head" style="left:0;right:0;text-align:center;top:33px;font-size:8.6px">Kurzbeschreibung des Angebotes</div>
  <div class="rule center" style="left:26px;right:26px;top:50px"></div>
  <div class="label" style="left:37px;top:72px">Lagebeschreibung</div>
  <div class="body" style="left:92px;top:72px;width:95px">
    <p>Das geschmackvolle, einseitig angebaute 5½-Zimmer Einfamilienhaus wirkt äusserst modern und grosszügig, ohne dabei auf angenehme Leichtigkeit zu verzichten.</p>
    <p>Leicht oberhalb des Zentrums, nahe unzähligen Wäldern, Feldern und Rebbergen, befindet sich Ihr neues Zuhause. Trotz der erhöhten Lage erreichen Sie das Zentrum mit Läden, Bahnhof, Schulen und Kindergarten innert zehn Gehminuten. Bequemer geht es mit dem Bus.</p>
    <p>Dieser bietet direkten Anschluss an die S-Bahn. Die Stadt erreichen Sie bestens mittels ÖV oder dem Auto.</p>
  </div>
  <div class="label" style="left:37px;top:174px">Objektbeschreibung</div>
  <div class="body" style="left:92px;top:174px;width:95px">
    <p>Der moderne und doch dezent gehaltene Innenausbau weiss mit hochwertigen Materialien und einem durchdachten Raumkonzept zu überzeugen.</p>
    <p>Die Schlaf- und Wohnräume verteilen sich über drei Etagen, zuzüglich dem überaus grosszügigen Untergeschoss. Lichtdurchflutete Räume dank bodentiefen Fenstern, eine offene Küche mit angrenzendem Wohnbereich, moderne Nassräume, grosszügige Kinderzimmer, ein Elternschlafzimmer mit Ankleide und eigenem Bad sorgen für ein Wohlgefühl auf höchstem Niveau.</p>
    <p>Umgeben wird dieses Schmuckstück von einem pflegeleichten, ganztägig besonnten Garten mit Sitzplätzen, Spielmöglichkeit für Kinder, Kräutergarten und Dachterrasse.</p>
  </div>
  <div class="footer-url">www.quorlanta.com</div>
  <div class="brand footer-brand">Quorlanta</div>
  <div class="footer-rule"></div>
</section>

<!-- Floor plan -->
<section class="page p5">
  <div class="head" style="left:0;right:0;text-align:center;top:36px;font-size:8.6px">Grundriss zweites Obergeschoss</div>
  <div class="rule center" style="left:25px;right:25px;top:52px"></div>
  <div class="photo" role="img" aria-label="Grundriss des zweiten Obergeschosses mit Möblierung" style="left:21px;top:65px;width:96px;height:107px;background:linear-gradient(#f6eec9,#efe3b4);border:1px solid #e4dcc0"></div>
  <div class="abs" style="left:126px;top:69px;font-size:7.5px;font-weight:500;color:var(--green)">Die Hypothek</div>
  <div class="body" style="left:126px;top:81px;width:76px;line-height:9px">
    <p>Das Angebot wurde durch BRANDT &amp; KELLER bewertet und für gut befunden.</p>
    <p>Der Kaufpreis in der Höhe von Total CHF 2'280'000.- (inkl. zwei Tiefgaragenplätze) wurde durch verschiedene Banken geprüft. Bitte beachten Sie die Empfehlungsschreiben im Anhang.</p>
  </div>
  <div class="abs" style="left:25px;top:193px;font-size:11px;font-weight:500;color:var(--green)">Konditionen</div>
  <div class="label" style="left:25px;top:218px">Übergabedatum</div>
  <div class="body" style="left:77px;top:218px;width:125px;font-size:4.2px">Die Übergabe findet nach Vereinbarung statt.</div>
  <div class="label" style="left:25px;top:241px">Verkaufspreis</div>
  <div class="body" style="left:77px;top:238px;width:125px;font-size:4.2px;line-height:5.6px;text-align:left">Der Verkaufspreis beträgt Total CHF 2'280'000.- inkl. zwei Tiefgaragenplätze.</div>
  <div class="label" style="left:25px;top:266px">Kosten</div>
  <div class="body" style="left:77px;top:263px;width:125px;font-size:4.2px;line-height:5.6px;text-align:left">Notariats- und Grundbuchgebühren gehen je zur Hälfte zu Lasten der Verkäuferschaft und Käuferschaft.</div>
  <div class="footer-url">www.quorlanta.com</div>
  <div class="brand footer-brand">Quorlanta</div>
  <div class="footer-rule"></div>
</section>

<!-- Mortgage A -->
<section class="page p6">
  <svg class="shapes" width="222" height="311" viewBox="0 0 222 311">
    <polygon points="132,0 222,0 222,40 202,125 160,30 140,0" fill="var(--lime)"/>
    <polygon points="140,0 152,0 196,100 202,125 160,30" fill="var(--green)"/>
    <polygon points="176,22 202,125 222,40 222,5" fill="var(--deep)"/>
  </svg>
  <div class="photo" role="img" aria-label="Foto der Dachterrasse mit Seesicht" style="left:25px;top:24px;width:140px;height:93px;background:linear-gradient(#b88a5a 0%,#d0c8b8 8%,#8fb6df 25%,#5c87a8 45%,#4f7a3d 62%,#b0704a 80%,#9a5e3e)"></div>
  <div class="head" style="left:17px;top:128px;font-size:7px">Die Hypothek</div>
  <div class="body" style="left:17px;top:141px;width:98px;line-height:4.4px">
    <p>Das Angebot wurde durch BRANDT &amp; KELLER bewertet und für gut befunden.</p>
    <p style="margin-top:8px">Der Kaufpreis in der Höhe von Total CHF 2'280'000.- (inkl. Tiefgaragenplätze) wurde durch verschiedene Banken geprüft. Bitte beachten Sie die verschiedenen Empfehlungsschreiben im Anhang.</p>
    <p style="margin-top:8px">Einfacher geht es nicht! BRANDT &amp; KELLER IMMOBILIEN unternehmen alles, damit Sie den Kauf Ihres Objektes rasch und mit geringem Aufwand realisieren können.</p>
    <p>Weitere Informationen finden Sie unter www.seeufer-wohnen.ch.</p>
    <p style="margin-top:8px">Möchten Sie wissen, was Ihre Immobilie wert ist? Dann setzen Sie sich mit uns für eine unverbindliche und kostenlose Immobilienbewertung in Verbindung.</p>
  </div>
  <div class="framed" style="left:127px;top:143px;width:83px;height:57px"><div class="photo" role="img" aria-label="Foto des Wohnzimmers mit Sofa" style="background:linear-gradient(#dfe6ec,#c7a17e 60%,#8a4a3a)"></div></div>
  <div class="framed" style="left:127px;top:208px;width:83px;height:57px"><div class="photo" role="img" aria-label="Foto des Essbereichs mit Seeblick" style="background:linear-gradient(#e9ecee,#aab9c4 50%,#5b4a40)"></div></div>
  <div class="footer-url">www.quorlanta.com</div>
  <div class="brand footer-brand">Quorlanta</div>
  <div class="footer-rule"></div>
</section>

<!-- Mortgage B -->
<section class="page p7">
  <div class="framed" style="left:31px;top:19px;width:160px;height:115px;padding:8px">
    <div class="photo" role="img" aria-label="Foto der Küche mit Esstisch und Seeblick" style="background:linear-gradient(90deg,#f1f1ef 0%,#e5e3dc 55%,#cfd8c0 75%,#e8ece6);"></div>
  </div>
  <div class="head" style="left:30px;top:139px;font-size:7px">Die Hypothek</div>
  <div class="body" style="left:30px;top:151px;width:160px;line-height:4.3px">
    <p>Das Angebot wurde durch BRANDT &amp; KELLER bewertet und für gut befunden.</p>
    <p style="margin-top:10px">Der Kaufpreis in der Höhe von Total CHF 2'280'000.- (inkl. zwei Tiefgaragenplätze) wurde durch verschiedene Banken geprüft. Bitte beachten Sie die Empfehlungsschreiben im Anhang.</p>
    <p style="margin-top:10px">Einfacher geht es nicht! BRANDT &amp; KELLER IMMOBILIEN unternehmen alles, damit Sie den Kauf Ihres Objektes rasch und mit geringem Aufwand realisieren können.</p>
    <p>Weitere Informationen finden Sie unter www.seeufer-wohnen.ch.</p>
    <p style="margin-top:10px">Möchten Sie wissen, was Ihre Immobilie wert ist? Dann setzen Sie sich mit uns für eine unverbindliche und kostenlose Immobilienbewertung in Verbindung.</p>
  </div>
  <div class="framed" style="left:30px;top:246px;width:45px;height:31px;padding:2px"><div class="photo" role="img" aria-label="Foto des Wohnraums" style="background:linear-gradient(#dfe4e8,#b58462)"></div></div>
  <div class="framed" style="left:89px;top:246px;width:45px;height:31px;padding:2px"><div class="photo" role="img" aria-label="Foto des Wohnzimmers" style="background:linear-gradient(#e2dcd2,#a86a4e)"></div></div>
  <div class="framed" style="left:147px;top:246px;width:45px;height:31px;padding:2px"><div class="photo" role="img" aria-label="Foto des Badezimmers" style="background:linear-gradient(#eceff1,#9aa3a8)"></div></div>
  <div class="footer-url">www.quorlanta.com</div>
  <div class="brand footer-brand">Quorlanta</div>
  <div class="footer-rule"></div>
</section>

<!-- Back cover -->
<section class="page p8">
  <svg class="shapes" width="222" height="311" viewBox="0 0 222 311">
    <defs><linearGradient id="backPhoto" x1="0" y1="0" x2="0" y2="1"><stop offset="0" stop-color="#5aad48"/><stop offset="1" stop-color="#2f8a2f"/></linearGradient></defs>
    <polygon points="0,0 222,0 222,72 121,225 0,128" fill="url(#backPhoto)" role="img" aria-label="Foto des Gartens mit grossem Baum, grün getönt"/>
    <polygon points="222,72 222,100 128,236 121,225" fill="#ebebeb"/>
    <polygon points="0,128 112,218 60,311 0,311" fill="var(--lime)"/>
  </svg>
  <div class="brand abs" style="left:110px;top:148px;font-size:24px;color:var(--lime);transform:rotate(-50deg);transform-origin:left top">Quorlanta</div>
  <div class="circle" role="img" aria-label="Foto des weissen Einfamilienhauses" style="left:32px;top:190px;width:66px;height:66px;border-width:4px;background:radial-gradient(circle at 50% 40%,#f2f3f4,#9bbf86 70%,#5d8c48)"></div>
  <div class="contact-name">JOHN DOE</div>
  <div class="contact-role">Manager</div>
  <ul class="contact-list">
    <li><svg width="5" height="5" viewBox="0 0 10 10"><circle cx="5" cy="5" r="5" fill="var(--green)"/><path d="M3.2 2.6l1 1-.6.7a4 4 0 0 0 2 2l.7-.6 1 1-.8.8C4.8 7.3 2.7 5.2 2.5 3.4z" fill="#fff"/></svg>111-222-333</li>
    <li><svg width="5" height="5" viewBox="0 0 10 10"><circle cx="5" cy="5" r="5" fill="var(--green)"/><rect x="2.5" y="3.3" width="5" height="3.4" fill="#fff"/><path d="M2.5 3.3L5 5.3 7.5 3.3" stroke="var(--green)" stroke-width=".6" fill="none"/></svg>info@quorlanta.com</li>
    <li><svg width="5" height="5" viewBox="0 0 10 10"><circle cx="5" cy="5" r="5" fill="var(--green)"/><path d="M5 2.2a2 2 0 0 1 2 2c0 1.5-2 3.6-2 3.6S3 5.7 3 4.2a2 2 0 0 1 2-2z" fill="#fff"/></svg>Your address, your city, box 88900</li>
  </ul>
</section>

</body>
</html>
```